Fatigued and Overloaded by COVID Messages? We need original illustrations to show that.

Everywhere you look there are messages about COVID. That is leading many people to feel fatigued and overloaded by the messages.

We surveyed U.S. adults March 20th - 24th, 2020 and measured message fatigue, information overload, perceived repetition, and perceived exaggeration. Here is how participants responded:

When it comes to coronavirus . . .
55% feel exhausted by all the messages.
54% feel overloaded by the amount of information.
51% feel that the messages are repetitive.
47% feel like messages exaggerate how bad it is.

In other words, almost half of U.S. adults show signs of message fatigue, information overload, perceived message repetition, and perceived message exaggeration.

We will continue to survey 400 adults every week for the next 16 weeks. Each time we will measure message fatigue, information overload, perceived repetition, and perceived exaggeration. We expect that it will increase over time.

What are we looking for? We need innovative and original illustrations that attempt to communicate these findings. The illustrations would visualize message fatigue, information overload, perceived message repetition, and perceived message exaggeration.

What sort of visual are we looking for? Our preference is for an original illustration (or set of illustrations). Our preference is for creative and powerful illustrations, but we are also open to the creative and well-executed infographics.

We need these images fast . We will award monetary prizes to the 3 best designs. If we like more than that, then we might purchase more (e.g., in past contests, we have purchased as many as 30 designs).

What we will need:
(1) The illustrations must be original and we will need the photoshop and/or illustrator files for all artwork. (By original, we mean that the illustrations are 100% created by you. Our organization requires that we utilize only original illustrated work. We have had issues with free imagery being pirated and reposted as free. We sidestep that issue by just having everything created.)

(2) The illustration should say, somewhere: "Based on a survey of 400 U.S. adults conducted March 20 - 24th, 2020."

(3) We will have almost 4 months worth of data by the time this is done. In other words, the illustrations might be able to help us present that weekly data.

(4) We have conducted other Artvendo projects. It might be helpful to examine designs we liked in the past. For example, here is another COVID project we just finished:

https://jobs.artvendo-example.com/job/5162048

Target Market(s)

U.S. adults

Requirements
Must have
• Original illustrations. Mobile friendly design. People will view this on their smartphones.
Nice to have
• A design that we can use to communicate the data across time.

```html
<!DOCTYPE html>
<html lang="en">
<head>
<meta charset="utf-8">
<title>Fatigued and Overloaded by COVID Messages</title>
<link rel="stylesheet" href="https://fonts.googleapis.com/css2?family=Amatic+SC:wght@700&family=Almendra+SC&family=Caesar+Dressing&display=swap">
<style>
:root{
  --page:#f2e92a;
  --ink:#0b0b0b;
  --blue:#175a8c;
  --blue-soft:#1f6a9e;
  --red:#e8202e;
  --red-soft:#f03a45;
  --bar-yellow:#fdf200;
  --white:#ffffff;
  --ghost:#cdbf3a;
}
*{box-sizing:border-box;margin:0;padding:0}
html,body{width:713px;height:1200px;overflow:hidden;background:var(--page)}
.poster{position:relative;width:713px;height:1200px;background:var(--page);font-family:"Almendra SC",serif;color:var(--ink)}
.abs{position:absolute}
.title-band{left:21px;top:21px;width:663px;height:132px;background:var(--ink);display:flex;align-items:center;justify-content:center}
.title{font-family:"Amatic SC",cursive;font-weight:700;color:var(--white);font-size:60px;line-height:50px;text-align:center;letter-spacing:1px;padding-top:4px}
.virus{border-radius:50%}
.virus-white{background:var(--white)}
.virus-yellow{background:var(--page)}
.virus-ghost{background:var(--ghost);opacity:.55}
.section-tag{left:110px;top:175px;width:489px;height:64px;background:var(--ink);color:var(--white);font-size:33px;font-weight:400;text-transform:lowercase;display:flex;align-items:center;justify-content:center;letter-spacing:3px;white-space:nowrap}
.spot-blue{background:radial-gradient(circle at 45% 45%,var(--blue-soft),var(--blue));border-radius:46% 54% 42% 58% / 52% 44% 56% 48%}
.spot-red{background:radial-gradient(circle at 50% 45%,var(--red-soft),var(--red));border-radius:55% 45% 50% 50% / 45% 55% 45% 55%}
.bar{border:5px solid var(--ink);display:flex;background:var(--ink)}
.bar-fill{background:var(--bar-yellow);display:flex;align-items:center;justify-content:center;font-family:"Caesar Dressing",cursive;font-size:32px}
.bar-rest{flex:1}
.rest-red{background:var(--red)}
.rest-blue{background:var(--blue)}
.pct-blue{color:var(--blue)}
.pct-red{color:var(--red)}
.label{font-size:30px;line-height:30px;text-align:center;letter-spacing:1.5px;text-transform:lowercase;white-space:nowrap;width:470px}
.summary{left:14px;top:930px;width:681px;height:97px;background:var(--red);color:var(--white);font-size:20px;line-height:24px;letter-spacing:1px;text-transform:lowercase;text-align:center;display:flex;align-items:center;justify-content:center;font-weight:700;white-space:nowrap}
.outlook{left:14px;top:1037px;width:681px;height:100px;background:var(--blue);color:var(--white);font-size:19px;line-height:24px;text-align:center;display:flex;align-items:center;justify-content:center;letter-spacing:1px;text-transform:lowercase;white-space:nowrap}
.source{left:18px;top:1144px;width:677px;height:47px;background:var(--ink);color:var(--white);font-size:18px;display:flex;align-items:center;justify-content:center;letter-spacing:1.5px;text-transform:lowercase;white-space:nowrap}
</style>
</head>
<body>
<main class="poster">
  <div class="abs virus-ghost virus" style="left:400px;top:420px;width:60px;height:60px" role="img" aria-label="faint virus decoration"></div>
  <div class="abs virus-ghost virus" style="left:215px;top:520px;width:160px;height:140px" role="img" aria-label="faint virus decoration"></div>
  <div class="abs virus-ghost virus" style="left:255px;top:720px;width:70px;height:60px" role="img" aria-label="faint virus decoration"></div>

  <header class="abs title-band">
    <h1 class="title">Fatigued and Overloaded<br>by COVID Messages</h1>
  </header>
  <div class="abs virus virus-white" style="left:58px;top:95px;width:40px;height:36px" role="img" aria-label="white virus decoration"></div>
  <div class="abs virus virus-white" style="left:640px;top:45px;width:28px;height:26px" role="img" aria-label="white virus decoration"></div>
  <div class="abs virus virus-yellow" style="left:588px;top:95px;width:50px;height:48px" role="img" aria-label="yellow virus decoration"></div>

  <h2 class="abs section-tag">Participants Responded</h2>

  <div class="abs spot-blue" style="left:61px;top:250px;width:181px;height:164px" role="img" aria-label="illustration: a worn-out person beneath a pile of social media message icons"></div>
  <div class="abs bar" style="left:264px;top:267px;width:349px;height:47px">
    <div class="bar-fill pct-blue" style="width:191px">55%</div><div class="bar-rest rest-red"></div>
  </div>
  <p class="abs label" style="left:204px;top:322px">Feel exhausted<br>by all the messages</p>

  <div class="abs spot-red" style="left:474px;top:389px;width:168px;height:189px" role="img" aria-label="illustration: a person buried under incoming news, documents and charts"></div>
  <div class="abs bar" style="left:93px;top:442px;width:345px;height:48px">
    <div class="bar-fill pct-red" style="width:187px">54%</div><div class="bar-rest rest-blue"></div>
  </div>
  <p class="abs label" style="left:30px;top:497px">Feel overloaded by<br>the amount of information</p>

  <div class="abs spot-blue" style="left:71px;top:578px;width:171px;height:181px" role="img" aria-label="illustration: a frustrated person circled by repeating phone and chat messages"></div>
  <div class="abs bar" style="left:264px;top:605px;width:349px;height:45px">
    <div class="bar-fill pct-blue" style="width:177px">51%</div><div class="bar-rest rest-red"></div>
  </div>
  <p class="abs label" style="left:204px;top:659px">Feel that the<br>messages are repetitive</p>

  <div class="abs spot-red" style="left:463px;top:724px;width:214px;height:192px" role="img" aria-label="illustration: a worried person thinking about alarming news headlines"></div>
  <div class="abs bar" style="left:93px;top:777px;width:345px;height:47px">
    <div class="bar-fill pct-red" style="width:159px">47%</div><div class="bar-rest rest-blue"></div>
  </div>
  <p class="abs label" style="left:30px;top:830px">Feel like messages<br>exaggerate how bad it is</p>

  <p class="abs summary">In other words, almost half of U.S. adults<br>show signs of message fatigue, information overload,<br>perceived message repetition, and perceived message exaggeration</p>

  <p class="abs outlook">We will continue to survey 400 adults every week for<br>the next 16 weeks. Each time we will measure message fatigue,<br>information overload, perceived repetition, and perceived<br>exaggeration. We expect that it will increase over time</p>

  <p class="abs source">This survey is based on U.S. adults from March 20th - 24th, 2020</p>
</main>
</body>
</html>
```